Pest Control Company needs business card!

Hi there, we need a business card designed for our new Pest Control Company. Ideally this card will be simple, yet feel elegant and high end. We want to use the colours Orange, Black and White. Please see our attached logo for the exact colours.

Business card details:

Phone - 0461 275 804
Name - Gavin Holloway
Email - Info@steadfastverminguard.com.au

We would also like to include the following list with dot points:

SERVICES / INSPECTIONS

Termites, Wood Borers, Ants, Cockroaches, Spiders, Fleas, Mice, Rats, Bed Bugs, & More!

```html
<!DOCTYPE html>
<html lang="en">
<head>
<meta charset="utf-8">
<title>Steadfast Vermin Guard – Business Card</title>
<link rel="stylesheet" href="https://fonts.googleapis.com/css2?family=Source+Sans+3:wght@400;600;700;800&display=swap">
<style>
  :root {
    --bg: #e2e2e2;
    --card-yellow: #f2d713;
    --card-white: #f4f4f4;
    --ink: #1d1c1a;
    --accent-red: #e31e26;
    --bubble: #ffffff;
  }
  * { box-sizing: border-box; margin: 0; padding: 0; }
  html, body {
    width: 1200px; height: 960px; overflow: hidden;
    background: var(--bg);
    font-family: "Source Sans 3", "Open Sans", Arial, sans-serif;
    color: var(--ink);
  }
  .canvas { position: relative; width: 1200px; height: 960px; }
  .card {
    position: absolute; left: 310px; width: 572px; height: 350px; overflow: hidden;
  }
  .card--front { top: 118px; background: var(--card-yellow); }
  .card--back { top: 508px; background: var(--card-white); }

  .card__art { position: absolute; inset: 0; }

  .services { position: absolute; left: 63px; top: 124px; font-size: 15px; line-height: 22.5px; }
  .services__title { font-weight: 700; font-size: 15.5px; letter-spacing: .1px; margin-bottom: 1px; }
  .services__line { font-weight: 400; }
  .bullet { color: var(--accent-red); padding: 0 2px; }

  .brand {
    position: absolute; left: 48px; top: 126px;
    font-weight: 800; font-size: 27px; line-height: 27px;
    text-transform: uppercase; color: var(--ink); letter-spacing: -.3px;
  }
  .divider { position: absolute; left: 285px; top: 117px; width: 2px; height: 117px; background: var(--card-yellow); }
  .contact { position: absolute; left: 306px; top: 118px; }
  .contact__name { color: var(--accent-red); font-weight: 700; font-size: 19px; line-height: 24px; }
  .contact__role { font-size: 14.5px; line-height: 18px; margin-bottom: 14px; }
  .contact__item { display: flex; align-items: center; gap: 5px; font-size: 14.5px; line-height: 19px; }
  .contact__item svg { width: 13px; height: 13px; flex: none; }
</style>
</head>
<body>
<div class="canvas">

  <section class="card card--front">
    <svg class="card__art" viewBox="0 0 572 350" width="572" height="350">
      <defs>
        <radialGradient id="mascotTone" cx="0.6" cy="0.5" r="0.6">
          <stop offset="0" stop-color="#1d1c1a"/>
          <stop offset="0.7" stop-color="#1d1c1a" stop-opacity="0.85"/>
          <stop offset="1" stop-color="#f2d713" stop-opacity="0"/>
        </radialGradient>
      </defs>
      <rect x="300" y="20" width="272" height="330" fill="url(#mascotTone)" role="img" aria-label="Cartoon bug mascot illustration"/>
      <polygon points="222,95 262,100 268,138 240,108" fill="#ffffff"/>
      <polygon points="30,250 80,258 40,262" fill="#ffffff"/>
      <polygon class="bubble" fill="var(--bubble)"
        points="40,118 150,94 228,98 262,130 258,160 312,180 262,192 264,222 210,256 42,258 30,222 42,190 36,150"/>
    </svg>
    <div class="services">
      <div class="services__title">SERVICES / INSPECTIONS</div>
      <div class="services__line"><span class="bullet">•</span> Termites <span class="bullet">•</span> Wood Borers</div>
      <div class="services__line"><span class="bullet">•</span> Ants <span class="bullet">•</span> Cockroaches</div>
      <div class="services__line"><span class="bullet">•</span> Spiders <span class="bullet">•</span> Fleas <span class="bullet">•</span> Mice</div>
      <div class="services__line"><span class="bullet">•</span> Rats <span class="bullet">•</span> Bed Bugs &amp; More!</div>
    </div>
  </section>

  <section class="card card--back">
    <div class="brand">Steadfast<br>Vermin<br>Guard</div>
    <div class="divider"></div>
    <div class="contact">
      <div class="contact__name">Gavin Holloway</div>
      <div class="contact__role">Owner</div>
      <div class="contact__item">
        <svg viewBox="0 0 16 16"><path fill="var(--accent-red)" d="M3.6 1l2.4 3-1.4 1.8c.9 2 2.6 3.7 4.6 4.6L11 9l3 2.4-1.2 2.8C7 14 2 9 1.8 3.2z"/></svg>
        <span>0461 275 804</span>
      </div>
      <div class="contact__item">
        <svg viewBox="0 0 16 16"><rect x="1.5" y="3.5" width="13" height="9" fill="none" stroke="var(--accent-red)" stroke-width="1.6"/><path d="M1.5 3.5l6.5 5 6.5-5" fill="none" stroke="var(--accent-red)" stroke-width="1.6"/></svg>
        <span>Info@steadfastverminguard.com.au</span>
      </div>
      <div class="contact__item">
        <svg viewBox="0 0 16 16" fill="none" stroke="var(--accent-red)" stroke-width="1.4"><circle cx="8" cy="8" r="6.3"/><ellipse cx="8" cy="8" rx="2.8" ry="6.3"/><path d="M1.7 8h12.6M2.8 4.8h10.4M2.8 11.2h10.4"/></svg>
        <span>www.steadfastverminguard.com.au</span>
      </div>
    </div>
  </section>

</div>
</body>
</html>
```